Logo and Business Card Design for Innovative Corporate Law Firm

Valmor Advogados is a new, young and innovative law firm focused in corporate law, mainly helping start-ups in the incorporation process, liasing with strategic investors, funds, private equity and venture/seed capital businesses around the world.

We need a logo and business card design that correctly captures our modern and savvy, yet sober, approach to legal practice.

We are looking to starting with the logo and business card designs and further ahead move on to stationery, website etc.

We are located in São Paulo/Brazil, but we expect our logo and stationery design to be able to reach and connect to possible clients worldwide due to the international characteristic of our practice.

Be creative! We have no restrictions on colors, one-sided or two-sided cards, logos, font styles...
Updates

Guys, just to be clear: The project shall contemplate a full stationery design, but the logo and business card may be proposed in advance due to our urgent need to have these cards ready for our clients. The other stationery items may be proposed later on. Many thanks!

Dear all, please be aware that the logo should look good both in collor and black and white. 

Thanks

Industry/Entity Type

Business

Requirements
Must have
• Modern but sober approach
Nice to have
• I tend to like grey collor schemes with red touches, but this is not a must have...
Should not have
• Excessively bright, shiny look, that will make our legal services look too commercial. No excesses.

```html
<!DOCTYPE html>
<html lang="pt-BR">
<head>
<meta charset="utf-8">
<title>Valmor Advogados – Cartão de visita</title>
<link rel="stylesheet" href="https://fonts.googleapis.com/css2?family=Maven+Pro:wght@400;500&family=Euphoria+Script&display=swap">
<style>
  :root {
    --page: #ffffff;
    --olive-dark: #58594a;
    --olive-mid: #8e8e7e;
    --olive-light: #cfcfc2;
    --stone: #e4e4da;
    --wine: #7e0404;
    --ink: #1d1c1a;
    --paper-text: #ffffff;
  }
  * { margin: 0; padding: 0; box-sizing: border-box; }
  html, body {
    width: 1200px; height: 523px; overflow: hidden;
    background: var(--page);
  }
  .sheet { position: relative; width: 1200px; height: 523px; }
  .card {
    position: absolute; top: 57px; height: 293px; overflow: hidden;
    box-shadow: 0 2px 4px rgba(0,0,0,0.25);
  }
  .card--front { left: 36px; width: 544px; }
  .card--back { left: 618px; width: 552px; }

  .card__backdrop { position: absolute; inset: 0; }
  .card--front .card__backdrop {
    background: linear-gradient(30deg,
      var(--olive-light) 0%,
      var(--olive-mid) 35%,
      var(--olive-dark) 68%,
      var(--wine) 100%);
  }
  .card--back .card__backdrop {
    background: linear-gradient(35deg,
      var(--olive-light) 0%,
      var(--stone) 28%,
      var(--olive-mid) 48%,
      var(--wine) 62%,
      var(--wine) 100%);
  }

  .brand-name {
    position: absolute; left: 6px; bottom: 30px;
    font-family: "Maven Pro", sans-serif; font-weight: 400;
    font-size: 46px; letter-spacing: -0.5px;
    color: var(--ink);
  }

  .contact {
    position: absolute; left: 6px; top: 3px;
    font-family: "Maven Pro", sans-serif; font-weight: 400;
    font-size: 22px; line-height: 24px; color: var(--ink);
  }
  .contact__group { margin-bottom: 22px; }
  .contact__address { font-style: normal; }

  .holder-name {
    position: absolute; right: 8px; bottom: 14px;
    font-family: "Euphoria Script", cursive;
    font-size: 46px; color: var(--paper-text);
  }
</style>
</head>
<body>
<main class="sheet">

  <section class="card card--front" aria-label="Frente do cartão">
    <div class="card__backdrop" role="img" aria-label="Fundo decorativo em tons de oliva com toque vinho"></div>
    <p class="brand-name">Valmor Advogados</p>
  </section>

  <section class="card card--back" aria-label="Verso do cartão">
    <div class="card__backdrop" role="img" aria-label="Fundo decorativo em tons de pedra e vinho"></div>
    <div class="contact">
      <div class="contact__group">
        <p>contato@valmoradvogados.com.br</p>
        <p>www.valmoradvogados.com.br</p>
      </div>
      <div class="contact__group">
        <p>+ 55 11 4020-1736</p>
      </div>
      <address class="contact__address">
        <p>Rua das Acácias,</p>
        <p>820, Torre 3, Sala 214</p>
        <p>São Paulo/SP-CEP:</p>
        <p>04512-031</p>
      </address>
    </div>
    <p class="holder-name">Marcelo de Andrade Valmor</p>
  </section>

</main>
</body>
</html>
```